Formal expert report - construction legal and quantum matters

Formal expert report document.

Require a template which includes a front page, content page.

Front page should have logo, some construction pictures (attached).

Remaining pages should have logo and header/footer.

Styles should be set up also.

Letterhead attached for branding colours etc.

Target Market(s)

lawyers, tribunal, arbitrators, fellow experts.

Industry/Entity Type

Construction, legal, quantity surveying, expert

Font styles to use
Other font styles liked:
• Garamond writing style, (will consider a more readable smart modern/professional format)

Colors
0054AA
0677BA
7BADD7
CADEEF
E8F1F8

```html
<!DOCTYPE html>
<html lang="en">
<head>
<meta charset="utf-8">
<title>Expert Report Template – Page Set</title>
<link rel="stylesheet" href="https://fonts.googleapis.com/css2?family=Sora:wght@300;400;600;700&family=Figtree:wght@400;500&family=Tinos:wght@700&display=swap">
<style>
:root{
  --brand:#2b49ad;
  --brand-deep:#1f3690;
  --brand-soft:#7badd7;
  --ink:#1d1f24;
  --text:#6b6f78;
  --rule:#d9dbe0;
  --stage:#eeeff1;
  --white:#ffffff;
}
*{margin:0;padding:0;box-sizing:border-box}
html,body{width:971px;height:1200px;overflow:hidden}
body{background:var(--stage);position:relative;font-family:"Figtree",sans-serif;color:var(--ink)}
.page{position:absolute;width:241px;height:312px;background:var(--white);overflow:hidden}
.col-1{left:77px}.col-2{left:363px}.col-3{left:650px}
.row-1{top:77px}.row-2{top:444px}.row-3{top:811px}
.abs{position:absolute}
.layer{position:absolute;left:0;top:0;width:241px;height:312px}

/* cover */
.cover-name{left:0;width:241px;top:27px;text-align:center;font-family:"Sora",sans-serif;font-weight:300;font-size:22px;letter-spacing:5px;color:var(--brand-deep)}
.cover-title{left:20px;width:201px;top:76px;text-align:center;font-family:"Sora",sans-serif;font-weight:600;font-size:7.4px;line-height:10px;letter-spacing:.2px}
.cover-values{left:10px;width:221px;top:103px;text-align:center;font-family:"Figtree",sans-serif;font-size:6.1px;color:var(--brand)}
.cover-web{left:38px;width:163px;top:278px;height:14px;background:rgba(220,224,232,.55);color:var(--ink);font-size:4.6px;letter-spacing:3.2px;text-align:center;line-height:14px}

/* contents */
.contents-panel{left:20.5px;top:35.5px;width:201px;height:242px;background:rgba(226,226,234,.72)}
.contents-title{left:28.5px;top:62px;font-family:"Sora",sans-serif;font-weight:600;font-size:6.2px}
.contents-list{left:28.5px;top:81px;width:184px;list-style:none;font-size:4px;text-transform:uppercase}
.contents-list li{display:flex;align-items:flex-end;height:7.8px}
.contents-list .leader{flex:1;border-bottom:.5px dotted #555;margin:0 1px 1.3px}

/* shared inner page furniture */
.brand-mark{left:186px;top:12px;font-family:"Sora",sans-serif;font-size:4.4px;letter-spacing:.8px;color:#8190bb}
.client-slot{left:216px;top:5.5px;width:21px;height:19.5px;border:.6px dashed #9a9ca3;font-size:2px;color:#aaa;text-align:center;padding-top:6px;line-height:2.6px}
.heading-rule{left:26px;top:25.5px;width:62px;height:.8px;background:var(--brand)}
.heading{left:28.5px;top:39.5px;font-family:"Sora",sans-serif;font-weight:600;font-size:6px;letter-spacing:.3px}
.footer-copy{left:28.5px;top:292.5px;font-size:3.7px;color:var(--text)}
.page-no{left:196px;top:292.5px;font-size:3.7px;color:var(--text)}
.page-no b{font-weight:400;color:var(--brand);border-left:.5px solid var(--ink);padding-left:1px}
.footer-band{left:0;bottom:0;width:241px;height:9.5px;background:var(--brand)}

.body-copy{font-size:3.65px;line-height:5.4px;color:var(--text);text-align:justify}
.sub-heading{font-family:"Sora",sans-serif;font-weight:600;font-size:5.8px}
.chart-title{font-family:"Sora",sans-serif;font-weight:600;font-size:6.2px;color:var(--brand);text-align:center}

/* process boxes */
.step{width:62px;height:50px;border:1px solid var(--brand);top:130px;text-align:center;padding:13px 3px 0}
.step h4{font-family:"Tinos",serif;font-size:4.2px;color:#666;margin-bottom:3px}
.step p{font-size:2.9px;line-height:3.9px;color:var(--text)}
.step-icon{width:22px;height:22px;border-radius:50%;background:var(--brand);border:2px solid var(--white);box-shadow:0 0 0 .6px var(--brand);top:119px}

.donut-note{width:40px;text-align:center;font-size:2.7px;line-height:3.6px;color:var(--text);top:150px}

/* table */
.data-table{left:28.5px;top:63px;width:185px;border-collapse:collapse;font-size:3.8px;color:var(--text)}
.data-table th{background:var(--brand);color:var(--white);font-weight:500;height:8.8px}
.data-table td{height:8.8px;text-align:center;border-bottom:.5px solid var(--rule)}
.data-table td.row-label{background:var(--brand);color:var(--white);border-bottom:.5px solid #6a80c8}

.feature-col{width:48px;top:139px;font-size:2.8px;line-height:3.9px;color:var(--text);text-align:justify}
.bullet-list{left:36px;top:210px;width:177px;font-size:3.7px;line-height:5.4px;color:var(--text);padding-left:6px}

/* closing */
.closing-band{left:0;top:174.5px;width:241px;height:72.5px;background:rgba(43,73,173,.78)}
.closing-text{left:0;width:241px;top:183px;text-align:center;font-family:"Sora",sans-serif;font-weight:600;font-size:33px;color:var(--white);letter-spacing:1px}
</style>
</head>
<body>

<!-- Cover -->
<section class="page col-1 row-1">
  <div class="abs cover-name">CORVELL</div>
  <h1 class="abs cover-title">SPECIALIST CONSTRUCTION CONSULTANCY SERVICES</h1>
  <p class="abs cover-values">Commitment, Value, Quality, Experience, Service, Honesty</p>
  <svg class="layer" viewBox="0 0 241 312">
    <defs>
      <linearGradient id="cityNight" x1="0" y1="0" x2="0" y2="1">
        <stop offset="0" stop-color="#1a1f3d"/>
        <stop offset=".6" stop-color="#2a2c4a"/>
        <stop offset="1" stop-color="#5a3d4a"/>
      </linearGradient>
    </defs>
    <polygon points="0,186 120.5,119 241,186 241,312 0,312" fill="#2b49ad"/>
    <polygon points="0,201 120.5,131 241,201 241,312 0,312" fill="url(#cityNight)" role="img" aria-label="Night city skyline with illuminated towers and construction cranes"/>
  </svg>
  <div class="abs cover-web">www.corvell-consult.co.uk</div>
</section>

<!-- Contents -->
<section class="page col-2 row-1">
  <div class="layer" role="img" aria-label="Construction site with tower cranes against a dusk sky" style="background:linear-gradient(180deg,#2d2a4f 0%,#5b4d78 30%,#b08e8f 55%,#6b5a6c 75%,#1d1c2e 100%)"></div>
  <div class="abs contents-panel"></div>
  <h2 class="abs contents-title">Table of Contents</h2>
  <ul class="abs contents-list">
    <li>Introduction Heading 1<span class="leader"></span>2</li>
    <li>Your Title Here-1.1<span class="leader"></span>3</li>
    <li>Your Title Here-1.1.1<span class="leader"></span>4</li>
    <li>Chart Slide<span class="leader"></span>5</li>
    <li>Table Slide<span class="leader"></span>6</li>
    <li>Picture and Bullet Point Slide<span class="leader"></span>7</li>
    <li>Bullet Point<span class="leader"></span>7</li>
  </ul>
</section>

<!-- Introduction -->
<section class="page col-3 row-1">
  <div class="abs brand-mark">CORVELL</div>
  <div class="abs client-slot">Client<br>Logo<br>Here</div>
  <div class="abs heading-rule"></div>
  <h2 class="abs heading">INTRODUCTION HEADING 1</h2>
  <p class="abs body-copy" style="left:28.5px;top:66px;width:185px">Lorem ipsum dolor sit amet, consectetuer adipiscing elit. Maecenas porttitor congue massa. Fusce posuere, magna sed pulvinar ultricies, purus lectus malesuada libero, sit amet commodo magna eros quis urna.Nunc viverra imperdiet enim. Fusce est. Vivamus a tellus.Pellentesque habitant morbi tristique senectus et netus et malesuada fames ac turpis egestas. Proin pharetra nonummy pede. Mauris et orci.Aenean nec lorem. In porttitor. Donec laoreet nonummy augue.Suspendisse dui purus, scelerisque at, vulputate vitae, pretium mattis, nunc. Mauris eget neque at sem venenatis eleifend. Ut nonummy.Fusce aliquet pede non pede. Suspendisse dapibus lorem pellentesque magna. Integer nulla. Lorem ipsum dolor sit amet, consectetuer adipiscing elit. Maecenas porttitor congue massa. Fusce posuere, magna sed pulvinar ultricies, purus lectus malesuada libero, sit amet commodo magna eros quis urna.Nunc viverra imperdiet enim. Fusce est. Vivamus a tellus.Pellentesque habitant morbi tristique senectus et netus et malesuada fames ac turpis egestas. Proin pharetra nonummy pede. Mauris et orci.Aenean nec lorem. In porttitor. Donec laoreet nonummy augue.Suspendisse dui purus, scelerisque at, vulputate vitae, pretium mattis, nunc. Mauris eget neque at sem venenatis eleifend. Ut nonummy.Fusce aliquet pede non pede. Suspendisse dapibus lorem pellentesque magna. Integer nulla.</p>
  <p class="abs footer-copy">Copyright © 2023 Corvell Ltd. All rights reserved.</p>
  <p class="abs page-no">PAGE<b> 2</b></p>
  <div class="abs footer-band"></div>
</section>

<!-- Title 1.1 -->
<section class="page col-1 row-2">
  <div class="abs brand-mark">CORVELL</div>
  <div class="abs client-slot">Client<br>Logo<br>Here</div>
  <div class="abs heading-rule"></div>
  <h2 class="abs heading">YOUR TITLE HERE-1.1</h2>
  <p class="abs body-copy" style="left:28.5px;top:64px;width:85px">Lorem ipsum dolor sit amet, consectetuer adipiscing elit. Maecenas porttitor congue Massa. Fusce posuere, magna sed pulvinar ultricies, Purus lectus malesuada libero, sit amet commodo magna eros quis urna.Nunc viverra imperdiet enim. Fusce est. Vivamus a tellus.Pellentesque habitant morbi tristique senectus ET netus ET malesuada fames ac turpis egestas. Proin pharetra nonummy pede. Mauris ET orci.Aenean NEC lorem. In porttitor. Donec laoreet nonummy augue.Suspendisse dapibus Purus, scelerisque at, vulputate vitae, pretium mattis, nunc. Mauris egret neque at SEM venenatis eleifend. Ut nonummy.Fusce aliquet pede non pede. Suspendisse dapibus lorem pellentesque magna. Integer nulla. Lorem ipsum dolor sit amet, consectetuer adipiscing elit. Maecenas porttitor congue Massa. Fusce posuere, magna sed pulvinar ultricies, Purus lectus malesuada libero, sit amet commodo magna eros quis urna.Nunc viverra imperdiet enim. Fusce est. Vivamus a tellus.Pellentesque habitant morbi tristique senectus ET netus ET malesuada fames ac turpis egestas. Proin pharetra nonummy pede. Mauris ET orci.Aenean NEC lorem. In porttitor. Donec laoreet nonummy augue.Suspendisse dui Purus, scelerisque at, vulputate vitae, pretium mattis, nunc.</p>
  <p class="abs body-copy" style="left:128px;top:64px;width:85px">Mauris egret neque at SEM venenatis eleifend. Ut nonummy.Fusce aliquet pede non pede. Suspendisse dapibus lorem pellentesque magna. Integer nulla. Lorem ipsum dolor sit amet, consectetuer adipiscing elit. Maecenas porttitor congue Massa. Fusce posuere, magna sed pulvinar ultricies, Purus lectus malesuada libero, sit amet commodo magna eros quis urna.Nunc viverra imperdiet enim. Fusce est. Vivamus a tellus.Pellentesque habitant morbi tristique senectus ET netus ET malesuada fames ac turpis egestas. Proin pharetra nonummy pede. Mauris ET orci.Aenean NEC lorem. In porttitor. Donec laoreet nonummy augue.Suspendisse dui Purus, scelerisque at, vulputate vitae, pretium mattis, nunc. Mauris egret neque at SEM venenatis eleifend. Ut nonummy.Fusce aliquet pede non pede. Suspendisse dapibus lorem pellentesque magna. Integer nulla. Lorem ipsum dolor sit amet, consectetuer adipiscing elit. Maecenas porttitor congue Massa. Fusce posuere, magna sed pulvinar ultricies, Purus lectus malesuada libero, sit amet commodo magna eros quis urna.Nunc viverra imperdiet enim. Fusce est. Vivamus a tellus.Pellentesque habitant morbi tristique senectus ET netus ET malesuada fames ac ut</p>
  <p class="abs footer-copy">Copyright © 2023 Corvell Ltd. All rights reserved.</p>
  <p class="abs page-no">PAGE<b> 3</b></p>
  <div class="abs footer-band"></div>
</section>

<!-- Title 1.1.1 -->
<section class="page col-2 row-2">
  <div class="abs brand-mark">CORVELL</div>
  <div class="abs client-slot">Client<br>Logo<br>Here</div>
  <div class="abs heading-rule"></div>
  <h2 class="abs heading">YOUR TITLE HERE-1.1.1</h2>
  <p class="abs body-copy" style="left:28.5px;top:64px;width:185px">Lorem ipsum dolor sit amet, consectetuer adipiscing elit. Maecenas porttitor congue massa. Fusce posuere, magna sed pulvinar ultricies, purus lectus malesuada libero, sit amet commodo magna eros quis urna.Nunc viverra imperdiet enim. Fusce est. Vivamus a tellus.Pellentesque habitant morbi tristique senectus et netus et malesuada fames ac turpis egestas. Proin pharetra nonummy pede. Mauris et orci.Aenean nec lorem. In porttitor. Donec laoreet nonummy augue.Suspendisse dui purus, scelerisque at, vulputate vitae, pretium mattis, nunc. Mauris eget neque at sem venenatis eleifend. Ut nonummy.Fusce aliquet pede non pede. Suspendisse dapibus lorem pellentesque magna. Integer nulla.</p>

  <div class="abs step" style="left:29px"><h4>Your Text Here</h4><p>Lorem ipsum dolor sit amet, consectetuer adipiscing elit. Maecenas porttitor congue Massa.</p></div>
  <div class="abs step" style="left:93.5px"><h4>Your Text Here</h4><p>Lorem ipsum dolor sit amet, consectetuer adipiscing elit. Maecenas porttitor congue Massa.</p></div>
  <div class="abs step" style="left:157px;width:58px"><h4>Your Text Here</h4><p>Lorem ipsum dolor sit amet, consectetuer adipiscing elit. Maecenas porttitor congue Massa.</p></div>
  <div class="abs step-icon" style="left:50px"></div>
  <div class="abs step-icon" style="left:114px"></div>
  <div class="abs step-icon" style="left:175px"></div>
  <svg class="layer" viewBox="0 0 241 312" fill="none" stroke="#fff" stroke-width=".9" stroke-linecap="round" stroke-linejoin="round">
    <!-- bulb -->
    <circle cx="61" cy="128" r="3.2"/><path d="M59.6 131.5v2h2.8v-2M59.8 135h2.4"/>
    <!-- target -->
    <circle cx="125" cy="130" r="4"/><circle cx="125" cy="130" r="1.8"/><path d="M125 130l4-4M127.5 126h1.5v-1.5"/>
    <!-- gears -->
    <circle cx="184.5" cy="131.5" r="2.2"/><circle cx="188" cy="127.5" r="1.6"/><circle cx="184.5" cy="131.5" r=".6" fill="#fff"/>
    <!-- arrows -->
    <path d="M89 151l4 4-4 4" stroke="#2a2c33" stroke-width="1.8"/>
    <path d="M153 151l4 4-4 4" stroke="#2a2c33" stroke-width="1.8"/>
  </svg>

  <p class="abs body-copy" style="left:28.5px;top:192px;width:185px">Lorem ipsum dolor sit amet, consectetuer adipiscing elit. Maecenas porttitor congue massa. Fusce posuere, magna sed pulvinar ultricies, purus lectus malesuada libero, sit amet commodo magna eros quis urna.Nunc viverra imperdiet enim. Fusce est. Vivamus a tellus.Pellentesque habitant morbi tristique senectus et netus et malesuada fames ac</p>
  <p class="abs footer-copy">Copyright © 2023 Corvell Ltd. All rights reserved.</p>
  <p class="abs page-no">PAGE<b> 4</b></p>
  <div class="abs footer-band"></div>
</section>

<!-- Chart -->
<section class="page col-3 row-2">
  <div class="abs brand-mark">CORVELL</div>
  <div class="abs client-slot">Client<br>Logo<br>Here</div>
  <div class="abs heading-rule"></div>
  <h2 class="abs heading">CHART SLIDE</h2>
  <p class="abs body-copy" style="left:28.5px;top:64px;width:185px">Lorem ipsum dolor sit amet, consectetuer adipiscing elit. Maecenas porttitor congue Massa. Fusce posuere, magna sed pulvinar ultricies, Purus lectus malesuada libero, sit amet commodo magna eros quis urna.Nunc viverra imperdiet enim. Fusce est. Vivamus a tellus.Pellentesque habitant morbi tristique senectus ET netus ET malesuada fames ac</p>

  <svg class="layer" viewBox="0 0 241 312" font-family="Sora, sans-serif">
    <g transform="translate(57.6 125)">
      <circle r="16.5" fill="none" stroke="#dcdde2" stroke-width="6"/>
      <circle r="16.5" fill="none" stroke="#2b49ad" stroke-width="6" stroke-dasharray="77.8 103.7" transform="rotate(-90)"/>
      <text y="2.2" text-anchor="middle" font-size="6" font-weight="700" fill="#2b49ad">75%</text>
    </g>
    <g transform="translate(122 125)">
      <circle r="16.5" fill="none" stroke="#dcdde2" stroke-width="6"/>
      <circle r="16.5" fill="none" stroke="#1f3690" stroke-width="6" stroke-dasharray="88.1 103.7" transform="rotate(-90)"/>
      <text y="2.2" text-anchor="middle" font-size="6" font-weight="700" fill="#2b49ad">85%</text>
    </g>
    <g transform="translate(185.7 125)">
      <circle r="16.5" fill="none" stroke="#dcdde2" stroke-width="6"/>
      <circle r="16.5" fill="none" stroke="#2b49ad" stroke-width="6" stroke-dasharray="57 103.7" transform="rotate(-90)"/>
      <text y="2.2" text-anchor="middle" font-size="6" font-weight="700" fill="#2b49ad">55%</text>
    </g>

    <!-- bar chart -->
    <g stroke="#e3e5ea" stroke-width=".4">
      <line x1="45" y1="217.6" x2="205" y2="217.6"/><line x1="45" y1="226.5" x2="205" y2="226.5"/>
      <line x1="45" y1="235.4" x2="205" y2="235.4"/><line x1="45" y1="244.2" x2="205" y2="244.2"/>
      <line x1="45" y1="253.1" x2="205" y2="253.1"/><line x1="45" y1="262" x2="205" y2="262"/>
    </g>
    <g font-size="3" fill="#666" font-family="Figtree, sans-serif" text-anchor="end">
      <text x="40" y="219">5</text><text x="40" y="227.5">4</text><text x="40" y="236.5">3</text>
      <text x="40" y="245.3">2</text><text x="40" y="254.2">1</text><text x="40" y="263">0</text>
    </g>
    <g>
      <rect x="49" y="223.8" width="8" height="38.2" fill="#2b49ad"/><rect x="57" y="239.8" width="8" height="22.2" fill="#3a4352"/><rect x="65" y="244.2" width="8" height="17.8" fill="#3c5bc4"/>
      <rect x="89" y="239.8" width="8" height="22.2" fill="#2b49ad"/><rect x="97" y="222.9" width="8" height="39.1" fill="#3a4352"/><rect x="105" y="246" width="8" height="16" fill="#3c5bc4"/>
      <rect x="129" y="230.9" width="8" height="31.1" fill="#2b49ad"/><rect x="137" y="244.2" width="8" height="17.8" fill="#3a4352"/><rect x="145" y="233.6" width="8" height="28.4" fill="#3c5bc4"/>
      <rect x="169" y="222" width="8" height="40" fill="#2b49ad"/><rect x="177" y="235.4" width="8" height="26.6" fill="#3a4352"/><rect x="185" y="217.6" width="8" height="44.4" fill="#3c5bc4"/>
    </g>
    <g font-size="2.9" fill="#666" font-family="Figtree, sans-serif" text-anchor="middle">
      <text x="65" y="267">Category 1</text><text x="105" y="267">Category 2</text>
      <text x="145" y="267">Category 3</text><text x="185" y="267">Category 4</text>
    </g>
  </svg>

  <p class="abs donut-note" style="left:37.6px">Lorem ipsum dolor sit amet, consectetuer adipiscing elit. Maecenas libero, sit amet</p>
  <p class="abs donut-note" style="left:102px">Lorem ipsum dolor sit amet, consectetuer adipiscing elit. Maecenas libero, sit amet</p>
  <p class="abs donut-note" style="left:165.7px">Lorem ipsum dolor sit amet, consectetuer adipiscing elit. Maecenas libero, sit amet</p>
  <p class="abs body-copy" style="left:28.5px;top:179px;width:185px">Lorem ipsum dolor sit amet, consectetuer adipiscing elit. Maecenas porttitor congue Massa. Fusce posuere, magna sed pulvinar ultricies, Purus lectus malesuada libero, sit a</p>
  <h3 class="abs chart-title" style="left:28.5px;width:190px;top:198.5px">Chart Title</h3>
  <p class="abs footer-copy">Copyright © 2023 Corvell Ltd. All rights reserved.</p>
  <p class="abs page-no">PAGE<b> 5</b></p>
  <div class="abs footer-band"></div>
</section>

<!-- Table -->
<section class="page col-1 row-3">
  <div class="abs brand-mark">CORVELL</div>
  <div class="abs client-slot">Client<br>Logo<br>Here</div>
  <div class="abs heading-rule"></div>
  <h2 class="abs heading">TABLE SLIDE</h2>
  <table class="abs data-table">
    <thead><tr><th></th><th>A</th><th>B</th><th>C</th><th>D</th></tr></thead>
    <tbody>
      <tr><td class="row-label">Content A</td><td>$67,000</td><td>200</td><td>400</td><td>800</td></tr>
      <tr><td class="row-label">Content B</td><td>$67,000</td><td>$56,000</td><td>$78,000</td><td>$90,000</td></tr>
      <tr><td class="row-label">Content C</td><td>4500</td><td>60000</td><td>$8,000</td><td>$20,000</td></tr>
      <tr><td class="row-label">Content D</td><td>34000</td><td>$400</td><td>$600</td><td>$1,200</td></tr>
      <tr><td class="row-label">Content E</td><td>$90</td><td>$800</td><td>$1,000</td><td>$3,400</td></tr>
    </tbody>
  </table>
  <p class="abs body-copy" style="left:28.5px;top:126.5px;width:185px">Lorem ipsum dolor sit amet, consectetuer adipiscing elit. Maecenas porttitor congue massa. Fusce posuere, magna sed pulvinar ultricies, purus lectus malesuada libero, sit amet commodo magna eros quis urna.Nunc viverra imperdiet enim. Fusce est. Vivamus a</p>
  <h3 class="abs chart-title" style="left:28.5px;width:142px;top:159px;font-size:7px">Chart Title</h3>
  <svg class="layer" viewBox="0 0 241 312" font-family="Figtree, sans-serif">
    <g stroke="#e3e5ea" stroke-width=".4">
      <line x1="31" y1="170" x2="212" y2="170"/><line x1="31" y1="182.2" x2="212" y2="182.2"/>
      <line x1="31" y1="194.3" x2="212" y2="194.3"/><line x1="31" y1="206.5" x2="212" y2="206.5"/>
      <line x1="31" y1="218.7" x2="212" y2="218.7"/><line x1="31" y1="230.8" x2="212" y2="230.8"/>
      <line x1="31" y1="243" x2="212" y2="243"/>
    </g>
    <g font-size="3.8" fill="#444" text-anchor="end">
      <text x="33" y="171.3">6</text><text x="33" y="183.5">5</text><text x="33" y="195.6">4</text>
      <text x="33" y="207.8">3</text><text x="33" y="220">2</text><text x="33" y="232.1">1</text><text x="33" y="244.3">0</text>
    </g>
    <g fill="none" stroke-width=".8">
      <path d="M59 190.7C74 190.7 88 212.6 103 212.6S131.5 200.4 146.5 200.4 175 188.2 190 188.2" stroke="#2b49ad"/>
      <path d="M59 213.8C74 213.8 88 189.5 103 189.5S131.5 221.1 146.5 221.1 175 208.9 190 208.9" stroke="#2b49ad"/>
      <path d="M59 218.7C74 218.7 88 218.7 103 218.7S131.5 206.5 146.5 206.5 175 182.2 190 182.2" stroke="#2a2c33"/>
    </g>
    <g fill="#2b49ad">
      <circle cx="59" cy="190.7" r="1"/><circle cx="103" cy="212.6" r="1"/><circle cx="146.5" cy="200.4" r="1"/><circle cx="190" cy="188.2" r="1"/>
      <circle cx="59" cy="213.8" r="1"/><circle cx="103" cy="189.5" r="1"/><circle cx="146.5" cy="221.1" r="1"/><circle cx="190" cy="208.9" r="1"/>
    </g>
    <g fill="#2a2c33"><circle cx="59" cy="218.7" r="1"/><circle cx="103" cy="218.7" r="1"/><circle cx="146.5" cy="206.5" r="1"/><circle cx="190" cy="182.2" r="1"/></g>
    <g font-size="4.2" fill="#444" text-anchor="middle">
      <text x="59" y="251">Category 1</text><text x="103" y="251">Category 2</text>
      <text x="146.5" y="251">Category 3</text><text x="190" y="251">Category 4</text>
    </g>
  </svg>
  <p class="abs footer-copy">Copyright © 2023 Corvell Ltd. All rights reserved.</p>
  <p class="abs page-no">PAGE<b> 6</b></p>
  <div class="abs footer-band"></div>
</section>

<!-- Picture and bullets -->
<section class="page col-2 row-3">
  <div class="abs brand-mark">CORVELL</div>
  <div class="abs client-slot">Client<br>Logo<br>Here</div>
  <div class="abs heading-rule"></div>
  <h2 class="abs heading">PICTURE AND BULLET POINT SLIDE</h2>
  <div class="abs" role="img" aria-label="Hands working over construction plans with building models" style="left:28px;top:61px;width:186px;height:67px;background:linear-gradient(135deg,#c9b3a6 0%,#d9dde6 45%,#a9b7cc 100%)"></div>
  <svg class="layer" viewBox="0 0 241 312">
    <g fill="#2b49ad" stroke="#fff" stroke-width="1">
      <polygon points="60,117.5 67.5,121.8 67.5,130.2 60,134.5 52.5,130.2 52.5,121.8"/>
      <polygon points="120,117.5 127.5,121.8 127.5,130.2 120,134.5 112.5,130.2 112.5,121.8"/>
      <polygon points="181,117.5 188.5,121.8 188.5,130.2 181,134.5 173.5,130.2 173.5,121.8"/>
    </g>
    <g fill="none" stroke="#fff" stroke-width=".7" stroke-linejoin="round">
      <path d="M56.5 126.5l7-3-3 7-1-3z"/>
      <path d="M121 122.5l-3 4.5h2.5l-1.5 4 3.5-5h-2.5z"/>
      <path d="M177.5 130h7M178.5 130v-3M180.5 130v-5M182.5 130v-4"/>
    </g>
  </svg>
  <p class="abs feature-col" style="left:36px">Lorem ipsum dolor sit amet, consectetuer adipiscing elit. Maecenas porttitor congue Massa. Fusce posuere, magna sed pulvinar ultricies, Purus lectus malesuada libero, sit amet commodo magna eros quis urna.Nunc viverra imperdiet enim. Fusce est. Vivamus a tellus.Pellentesque habitant morbi tristique senectus ET netus ET malesuada fames ac</p>
  <p class="abs feature-col" style="left:97px">Lorem ipsum dolor sit amet, consectetuer adipiscing elit. Maecenas porttitor congue Massa. Fusce posuere, magna sed pulvinar ultricies, Purus lectus malesuada libero, sit amet commodo magna eros quis urna.Nunc viverra imperdiet enim. Fusce est. Vivamus a tellus.Pellentesque habitant morbi tristique senectus ET netus ET malesuada fames ac</p>
  <p class="abs feature-col" style="left:158px">Lorem ipsum dolor sit amet, consectetuer adipiscing elit. Maecenas porttitor congue Massa. Fusce posuere, magna sed pulvinar ultricies, Purus lectus malesuada libero, sit amet commodo magna eros quis urna.Nunc viverra imperdiet enim. Fusce est. Vivamus a tellus.Pellentesque habitant morbi tristique senectus ET netus ET malesuada fames ac</p>
  <h3 class="abs sub-heading" style="left:28.5px;top:202.5px">BULLET POINT</h3>
  <ul class="abs bullet-list">
    <li>Lorem ipsum dolor sit amet, consectetuer adipiscing elit. Maecenas porttitor congue massa. Fusce posuere,</li>
    <li>magna sed pulvinar ultricies, purus lectus malesuada libero, sit amet commodo magna eros quis urna.Nunc</li>
    <li>viverra imperdiet enim. Fusce est. Vivamus a tellus.Pellentesque habitant morbi tristique senectus et net</li>
    <li>malesuada fames ac turpis egestas. Proin pharetra nonummy pede. Mauris et orci.Aenean nec lorem. In tristique senectus et netus et</li>
    <li>malesuada fames ac turpis egestas. Proin pharetra nonummy pede. Mauris et orci.Aenean nec lorem. In</li>
  </ul>
  <p class="abs footer-copy">Copyright © 2023 Corvell Ltd. All rights reserved.</p>
  <p class="abs page-no">PAGE<b> 7</b></p>
  <div class="abs footer-band"></div>
</section>

<!-- Closing -->
<section class="page col-3 row-3">
  <div class="layer" role="img" aria-label="Tower cranes silhouetted against a cloudy sunset sky" style="background:linear-gradient(180deg,#2c3530 0%,#4a5548 35%,#5e6658 55%,#2d3230 80%,#c98a2c 90%,#1a1a18 100%)"></div>
  <div class="abs closing-band"></div>
  <p class="abs closing-text">THANK YOU</p>
</section>

</body>
</html>
```